Visitenkarte und Briefdesign
Zielgruppe
Limousinenservice (Stretchlimousinen)
Aufgabenstellung
Ich benötige eine Visitenkarte und ein Briefdesign in einer edlen Optik.
Auf folgender Seite können Informationen oder Bilder eingeholt werden
www.karossa-fahrten.com
Ich mag einen Hintergrund in einer Lederoptik,( wie das Logo in Anhang, BILD x4)

```html
<!DOCTYPE html>
<html lang="de">
<head>
<meta charset="utf-8">
<title>Limousinenservice KR Loungecars – Briefbogen und Visitenkarte</title>
<link href="https://fonts.googleapis.com/css2?family=Jost:wght@400;600&family=Oswald:wght@300;500&display=swap" rel="stylesheet">
<style>
  :root {
    --leather-dark: #121212;
    --leather-mid: #2a2a2a;
    --paper: #ffffff;
    --ink: #111111;
    --muted: #7a7a7a;
    --chrome: #cfcfcf;
    --shadow: rgba(0,0,0,0.35);
  }
  * { box-sizing: border-box; margin: 0; padding: 0; }
  html, body { width: 849px; height: 1200px; overflow: hidden; background: var(--paper); }
  body { position: relative; font-family: "Jost", sans-serif; color: var(--ink); }

  .sheet { position: absolute; background: var(--paper); box-shadow: 6px 8px 10px var(--shadow); overflow: hidden; }
  .leather { position: absolute; left: 0; top: 0; width: 100%; }
  .leather-band { position: absolute; left: 0; bottom: 0; width: 100%; background: linear-gradient(180deg, var(--leather-mid), var(--leather-dark)); }

  .brand-mark { position: absolute; display: flex; align-items: center; gap: 5px; font-family: "Oswald", sans-serif; font-weight: 300; color: var(--chrome); letter-spacing: 0.06em; text-transform: uppercase; line-height: 1.05; }
  .brand-mark .dot { border-radius: 50%; border: 1.5px solid var(--chrome); flex: none; }

  .company-title { position: absolute; font-family: "Oswald", sans-serif; font-weight: 300; color: #fff; letter-spacing: 0.02em; white-space: nowrap; }
  .company-title strong { font-weight: 500; letter-spacing: 0.06em; }

  /* Letter */
  .letter { left: 112px; top: 39px; width: 626px; height: 884px; border: 1px solid #d8d8d8; }
  .letter .leather { height: 130px; }
  .letter .brand-mark { left: 52px; top: 30px; font-size: 13px; }
  .letter .brand-mark .dot { width: 26px; height: 26px; }
  .letter .company-title { right: 38px; top: 42px; font-size: 20px; }
  .sender-line { position: absolute; left: 60px; top: 160px; font-family: "Oswald", sans-serif; font-size: 6px; color: var(--muted); letter-spacing: 0.03em; }
  .recipient { position: absolute; left: 60px; top: 178px; font-size: 10.5px; line-height: 12.6px; letter-spacing: 0.04em; font-style: normal; }
  .recipient .city { margin-top: 13px; }
  .date { position: absolute; right: 38px; top: 280px; font-size: 11.5px; }
  .subject { position: absolute; left: 60px; top: 307px; font-size: 11.5px; font-weight: 600; letter-spacing: 0.02em; }
  .letter-body { position: absolute; left: 60px; top: 349px; width: 405px; font-size: 11.5px; line-height: 21px; }
  .letter-body p { text-align: justify; hyphens: auto; }
  .letter-body p + p { margin-top: 21px; }
  .letter-body .greeting { margin-bottom: 14px; }
  .closing { position: absolute; left: 60px; top: 692px; font-size: 11.5px; }
  .signature { position: absolute; left: 60px; top: 733px; font-size: 11.5px; }
  .footer-head { position: absolute; left: 0; width: 100%; top: 815px; text-align: center; font-size: 9px; color: var(--muted); word-spacing: 1px; }
  .footer-head span { margin: 0 12px; }
  .footer-grid { position: absolute; left: 41px; right: 20px; top: 833px; display: grid; grid-template-columns: 212px 183px 1fr; font-size: 8px; line-height: 12.5px; color: var(--muted); }
  .footer-grid dl { display: grid; grid-template-columns: 38px 1fr; }
  .letter .leather-band { height: 9px; }

  /* Business cards */
  .card { top: 943px; width: 344px; height: 223px; }
  .card-front { left: 64px; }
  .card-front .leather { height: 70px; }
  .card-front .brand-mark { left: 26px; top: 12px; font-size: 9px; }
  .card-front .brand-mark .dot { width: 18px; height: 18px; }
  .card-front .company-title { right: 12px; top: 33px; font-size: 12.5px; }
  .card-person { position: absolute; left: 0; top: 110px; width: 100%; text-align: center; font-family: "Oswald", sans-serif; }
  .card-person .name { font-size: 12px; letter-spacing: 0.04em; }
  .card-person .role { font-size: 7px; font-weight: 300; margin-top: 1px; }
  .card-contact { position: absolute; left: 0; top: 166px; width: 100%; text-align: center; font-family: "Oswald", sans-serif; font-weight: 300; font-size: 8px; line-height: 14px; }
  .card-contact b { font-weight: 500; margin-right: 3px; }
  .card-contact .gap { margin-left: 8px; }
  .card-front .leather-band { height: 8px; }

  .card-back { left: 455px; background: linear-gradient(160deg, var(--leather-mid), var(--leather-dark)); }
  .card-back .brand-mark { left: 0; top: 0; width: 100%; height: 100%; justify-content: center; font-size: 24px; gap: 10px; }
  .card-back .brand-mark .dot { width: 34px; height: 34px; border-width: 2px; }
</style>
</head>
<body>

<article class="sheet letter" aria-label="Briefbogen">
  <svg class="leather" viewBox="0 0 626 130" preserveAspectRatio="none" role="img" aria-label="Kopfband in schwarzer Lederstruktur">
    <defs>
      <linearGradient id="leatherHead" x1="0" y1="0" x2="0" y2="1">
        <stop offset="0" stop-color="#2a2a2a"/>
        <stop offset="1" stop-color="#121212"/>
      </linearGradient>
    </defs>
    <path d="M0 0H626V89Q313 160 0 89Z" fill="url(#leatherHead)"/>
  </svg>
  <div class="brand-mark"><span class="dot"></span><span>KR<br>Loungecars</span></div>
  <h1 class="company-title">LIMOUSINENSERVICE <strong>KR LOUNGECARS</strong></h1>

  <p class="sender-line">LIMOUSINENSERVICE KR LOUNGECARS – LINDENALLEE 42B – 48153 MÜNSTER</p>
  <address class="recipient">
    HERR<br>MAX MUSTERMANN<br>MUSTERSTRASSE 123
    <div class="city">12345 MUSTERSTADT</div>
  </address>
  <p class="date">Münster, den 12. Juli 2014</p>
  <h2 class="subject">Ihre Anfrage vom 01.06.2014</h2>

  <div class="letter-body">
    <p class="greeting">Sehr geehrte Damen und Herren,</p>
    <p>Nem nam inveliquat imintibus adis et lam et lia doluptatur? Lorrum ipid quas sequia alia volorep ellorro invelique aut quiduscil mo quis corrovit, que velenis dolorro rroviti onsequia si ilique volo moluptat elluptae venducia dolorei umquam faccae repero omni natumquae verrum diaspide aperem accuptat ex et aciis etur, sitem dolupicide doluptisti quatiae sam.</p>
    <p>Offic te voloriam elestios et experum earum volupta sperist ibusdae ipidelit fugi&shy;am, omnis ressus doluptatis eosandit molum hillese quiati repudis illupti nciatas a secto exerchi liquae ma dentisquos re, odigent, opti ute re prerrovid mo te volorib ustionseque et quiduciis ut porupta temolor andis dolenie ndenimus aute maximos est quia voluptas renienis ipid ut vellatque omnihitem nis aute vendellab ipsa&shy;perovid enducieniet laborro conseque que sinti sinciae volestrumqui a voluptatin conem fugia vit lat.</p>
  </div>
  <p class="closing">Mit freundlich Grüßen</p>
  <p class="signature">Jonas Keller</p>

  <footer>
    <p class="footer-head"><span>LIMOUSINENSERVICE KR LOUNGECARS</span><span>LINDENALLEE 42B</span><span>48153 MÜNSTER</span></p>
    <div class="footer-grid">
      <dl><dt>MAIL</dt><dd>info@kr-loungecars.de</dd><dt>TEL</dt><dd>+49 (0)170 555 0 147</dd><dt>WEB</dt><dd>www.karossa-fahrten.com</dd></dl>
      <div><div>Amtsgericht Münster</div><div>HRB XXXXX</div><div>Ust ID-Nr. DEXXXXXXX</div></div>
      <div class="bank"><div>Westfälische Stadtbank</div><dl><dt>IBAN</dt><dd>DEXX XXXX XXXX XXXX XXXX</dd><dt>BIC</dt><dd>XXXXXXXX</dd></dl></div>
    </div>
  </footer>
  <div class="leather-band" role="img" aria-label="Fußband in schwarzer Lederstruktur"></div>
</article>

<article class="sheet card card-front" aria-label="Visitenkarte Vorderseite">
  <svg class="leather" viewBox="0 0 344 70" preserveAspectRatio="none" role="img" aria-label="Kopfband in schwarzer Lederstruktur">
    <defs>
      <linearGradient id="leatherCard" x1="0" y1="0" x2="0" y2="1">
        <stop offset="0" stop-color="#2a2a2a"/>
        <stop offset="1" stop-color="#121212"/>
      </linearGradient>
    </defs>
    <path d="M0 0H344V50Q172 90 0 50Z" fill="url(#leatherCard)"/>
  </svg>
  <div class="brand-mark"><span class="dot"></span><span>KR<br>Loungecars</span></div>
  <h2 class="company-title">LIMOUSINENSERVICE <strong>KR LOUNGECARS</strong></h2>
  <div class="card-person">
    <p class="name">JONAS KELLER</p>
    <p class="role">- Inhaber -</p>
  </div>
  <div class="card-contact">
    <p>Lindenallee 42B<span class="gap"></span>48153 Münster</p>
    <p><b>MAIL</b>info@kr-loungecars.de<span class="gap"></span><b>TEL</b>+49 (0)170 555 0 147</p>
    <p><b>WEB</b>www.karossa-fahrten.com &nbsp;|&nbsp; www.kr-loungecars.de</p>
  </div>
  <div class="leather-band" role="img" aria-label="Fußband in schwarzer Lederstruktur"></div>
</article>

<article class="sheet card card-back" role="img" aria-label="Visitenkarte Rückseite in schwarzer Lederstruktur mit Firmenname">
  <div class="brand-mark"><span class="dot"></span><span>KR Loungecars</span></div>
</article>

</body>
</html>
```